"Retire With The Harrowgate Fund" Book Cover Design

This book is 5.5 x. 8.5 in size. Not enough room for any writing on the spine either. About 100 pages, and 18,000 words max.
The Harrowgate Fund goes back to 1930. In this book, I run scenario after scenario seeing what the best strategy was for someone to Retire With The Harrowgate Fund and never run out of money. And how they MIGHT be able to use this info to build a solid retirement plan using the Harrowgate Fund for themselves.
Target Market(s)
Soon-to-be and recent middle-class, married retirees.
Industry/Entity Type
Investment Advisory
Requirements
Must have
- MUST BE EYE CATCHING!
Should not have
- No Piggy Banks or old people sitting on a beach or any yachts.

```html
<!DOCTYPE html>
<html lang="en">
<head>
<meta charset="utf-8">
<title>Retire With The Harrowgate Fund – Cover Spread</title>
<link href="https://fonts.googleapis.com/css2?family=Playfair+Display:wght@500&family=Montserrat:wght@500;700;800&display=swap" rel="stylesheet">
<style>
  :root {
    --navy: #0f2d6b;
    --red: #e8201c;
    --white: #ffffff;
    --mist: #eef4f7;
    --ice: #d5e6ec;
    --stage: #e4e7e9;
  }
  html, body {
    margin: 0;
    width: 915px;
    height: 1200px;
    overflow: hidden;
    background: var(--stage);
  }
  .cover-spread {
    position: absolute;
    left: 0;
    top: 306px;
    width: 915px;
    height: 588px;
    display: block;
    box-shadow: 0 6px 18px rgba(0,0,0,.12);
  }
  .title-serif { font-family: "Playfair Display", Georgia, serif; font-weight: 500; fill: var(--navy); }
  .title-sans { font-family: "Montserrat", Arial, sans-serif; font-weight: 800; fill: var(--red); }
  .spine-title { font-family: "Montserrat", Arial, sans-serif; font-weight: 500; fill: var(--white); letter-spacing: 2px; }
  .author-label { font-family: "Montserrat", Arial, sans-serif; font-weight: 500; fill: var(--white); }
  .author-name { font-family: "Montserrat", Arial, sans-serif; font-weight: 700; fill: var(--white); }
</style>
</head>
<body>
<svg class="cover-spread" viewBox="0 0 1680 1080" xmlns="http://www.w3.org/2000/svg">
  <defs>
    <linearGradient id="sky" x1="0" y1="0" x2="1" y2="1">
      <stop offset="0" stop-color="#f4f8fa"/>
      <stop offset="0.5" stop-color="#eef4f6"/>
      <stop offset="1" stop-color="#f7f9fa"/>
    </linearGradient>
    <linearGradient id="cityscape" x1="0" y1="0" x2="0" y2="1">
      <stop offset="0" stop-color="#d8e8ee" stop-opacity="0.8"/>
      <stop offset="1" stop-color="#eef4f6" stop-opacity="0.2"/>
    </linearGradient>
    <linearGradient id="sketch" x1="0" y1="0" x2="1" y2="1">
      <stop offset="0" stop-color="#e6eef0"/>
      <stop offset="0.5" stop-color="#ecebe2"/>
      <stop offset="1" stop-color="#e4ecee"/>
    </linearGradient>
  </defs>

  <!-- background -->
  <rect class="page-bg" width="1680" height="1080" fill="url(#sky)"/>
  <rect class="city-photo" role="img" aria-label="Pale glass office towers and an open plaza" x="0" y="0" width="1680" height="820" fill="url(#cityscape)"/>

  <!-- translucent diamond panels -->
  <g class="diamond-panels" fill="#ffffff" fill-opacity="0.55" stroke="#ffffff" stroke-opacity="0.8">
    <rect x="60" y="-140" width="280" height="280" rx="40" transform="rotate(45 200 0)"/>
    <rect x="20" y="260" width="300" height="300" rx="40" transform="rotate(45 170 410)"/>
    <rect x="1330" y="520" width="280" height="280" rx="40" transform="rotate(45 1470 660)"/>
    <rect x="1500" y="-60" width="260" height="260" rx="40" transform="rotate(45 1630 70)"/>
  </g>

  <!-- sketch area -->
  <rect class="strategy-sketch" role="img" aria-label="Faint hand-drawn strategy sketch with charts, gears and icons" x="70" y="680" width="690" height="330" rx="30" fill="url(#sketch)" opacity="0.8"/>

  <!-- red sweep line -->
  <polyline class="red-sweep" points="0,148 805,228" fill="none" stroke="var(--red)" stroke-width="10"/>
  <polyline class="red-sweep" points="873,228 1680,145" fill="none" stroke="var(--red)" stroke-width="10"/>

  <!-- torn paper band -->
  <path class="torn-edge" fill="#ffffff" d="M0,975 L60,968 L110,978 L170,962 L230,968 L300,952 L360,958 L420,940 L500,945 L560,930 L640,928 L700,915 L760,912 L820,895 L880,895 L950,870 L1020,872 L1100,850 L1180,852 L1260,838 L1340,842 L1420,825 L1500,830 L1580,818 L1680,815 L1680,860 L0,1010 Z" filter="drop-shadow(0 3px 4px rgba(0,0,0,.3))"/>
  <path class="navy-band" fill="var(--navy)" d="M0,1005 L55,998 L110,1004 L170,990 L240,996 L300,982 L370,986 L430,970 L500,974 L570,958 L640,958 L710,945 L770,942 L830,926 L890,926 L960,902 L1030,904 L1110,882 L1190,884 L1270,868 L1350,872 L1430,856 L1510,860 L1590,848 L1680,846 L1680,1080 L0,1080 Z"/>

  <!-- spine -->
  <rect class="spine" x="805" y="-40" width="68" height="752" rx="34" fill="var(--navy)"/>
  <text class="spine-title" transform="translate(831 40) rotate(90)" font-size="27" textLength="640" lengthAdjust="spacingAndGlyphs">RETIRE WITH THE HARROWGATE FUND</text>
  <rect class="spine-slot" x="805" y="1020" width="68" height="100" rx="34" fill="#ffffff"/>

  <!-- title block -->
  <text class="title-serif" x="1250" y="235" font-size="100" text-anchor="middle" textLength="310" lengthAdjust="spacingAndGlyphs">RETIRE</text>
  <text class="title-serif" x="1222" y="330" font-size="100" text-anchor="middle" textLength="505" lengthAdjust="spacingAndGlyphs">WITH THE</text>
  <text class="title-sans" x="1250" y="415" font-size="78" text-anchor="middle" textLength="570" lengthAdjust="spacingAndGlyphs">HARROWGATE</text>
  <text class="title-serif" x="1255" y="575" font-size="175" text-anchor="middle" textLength="580" lengthAdjust="spacingAndGlyphs">FUND</text>

  <!-- author -->
  <text class="author-label" x="1228" y="980" font-size="26">AUTHER</text>
  <text class="author-name" x="1258" y="1032" font-size="48">DR. HOLLIS</text>
</svg>
</body>
</html>
```